Payment Processor Website Design

Our company LumaPort, an online processor of payments is seeking talented submissions for our website redesign. The winning design will be chopped up and converted into a WordPress theme to allow for easy content additions and updates.

We are looking for modern designs that rival current websites in our industry (qindle.example, ploverbank.example, zunmo.example, kelvory.example, mossfieldcharges.example, harrowlinecharges.example, TuxCoin.example).

Our company is seeking to expand our reach to software developers and engineers who are either integrating our payment platform into their offerings or are engineering a custom solution for the company they work for and are in need of a payment platform such as our own.

We currently work with hundreds of different business partners whom either resell our services or integrate our processing capabilities into their software (which they sell). We also must communicate effectively to end users, businesses, who seek us out directly for their payment processing needs.

We are open to different color schemes but would ultimately like them to be somewhat inline with our current logo (see attached). Our website needs to instill security and confidence to any current and/or potential user as we are trusted with private and sensitive information.

We are seeking submissions from qualified; individual freelancers, freelance teams, and agencies who can attack this project in its entirety. Since this project is a total redesign, we would like submissions that have the capability to design any custom graphics, icons, buttons, and illustrations in line with our industry, capabilities, offerings, and content. We are looking for someone to design our new website and would prefer a vendor who can also help us to design elements (graphics, illustrations, charts, workflows) within our website.

Designs will be converted into a wordpress theme and we would like to utilize widgets for as many areas as possible to make editing and updating easy.

We are seeking the creation of a few unique pages but many of the pages for the majority of our content will just be internal content pages which will be duplicated.

We will likely contract with the winning submission for future work.

Please see Design Reference Document for more information

Target Market(s)

Resellers
Merchant Service Providers
Software Developers
Independent Sales Organizations (ISOs)
App Builders
Mobile App Builders
Independent Software Developers
Organizational Software Developers
Businesses who need to accept payments
Governments
Municipalities
Schools
DMVs
Courts
Retailers
Medical Offices
Hosipitals
Clinics
Dr. Offices
Gyms
Churches
Non-Profits
Software Companies
Technology Companies
Startups

Industry/Entity Type

Industry

Requirements
Should not have
• Logo cannot change drastically.

```html
<!DOCTYPE html>
<html lang="en">
<head>
<meta charset="utf-8">
<title>LumaPort — Fast, Secure, Worldwide</title>
<link rel="stylesheet" href="https://fonts.googleapis.com/css2?family=Raleway:wght@400;500;600;700&family=Open+Sans:wght@400;600&display=swap">
<style>
:root{
  --navy:#1d2a78;
  --blue:#1d86d6;
  --blue-dark:#1569b0;
  --red:#d9191f;
  --ink:#2a2a2a;
  --muted:#555;
  --line:#dcdcdc;
  --gray-band:#eeeeee;
  --footer:#222222;
  --white:#ffffff;
}
*{box-sizing:border-box;margin:0;padding:0}
html,body{width:1074px;height:1200px;overflow:hidden}
body{position:relative;background:var(--white);font-family:"Open Sans",Arial,sans-serif;color:var(--ink)}
.abs{position:absolute}

/* top bar */
.topbar{left:0;top:0;width:1074px;height:44px;border-bottom:1px solid var(--line);background:var(--white)}
.brand{left:148px;top:8px;display:flex;align-items:center;gap:6px;font-family:"Raleway",sans-serif;font-weight:700;font-size:22px;color:var(--navy)}
.brand-dot{width:10px;height:10px;border-radius:50%;background:var(--red)}
.audience-tab{top:0;height:44px;display:flex;align-items:center;justify-content:center;font-family:"Raleway",sans-serif;font-size:12px;font-weight:500}
.tab-business{left:294px;width:103px;background:#ececec;color:#333}
.tab-developer{left:397px;width:103px;color:var(--blue);border-right:1px solid var(--line)}
.account-links{left:665px;top:15px;font-size:10px;color:#333}
.account-links span{margin:0 3px;color:#777}
.social{width:24px;height:24px;border-radius:50%;border:1px solid #bbb;background:#f5f5f5}

/* hero */
.hero{left:0;top:44px;width:1074px;height:469px;background:
  radial-gradient(ellipse 260px 330px at 760px 250px,#e9d3c2 0%,#d9c3b2 40%,rgba(220,225,220,0) 75%),
  linear-gradient(90deg,#dcecef 0%,#cfe6ea 35%,#e4eeee 60%,#d7e2e0 85%,#c9d8cf 100%)}
.main-nav{left:140px;top:69px;width:821px;height:40px;background:var(--white);border:1px solid var(--line);box-shadow:0 3px 5px rgba(0,0,0,.08);display:flex;align-items:center}
.main-nav a{position:absolute;font-family:"Raleway",sans-serif;font-size:12.5px;color:#333;text-decoration:none;top:12px}
.nav-sep{position:absolute;top:12px;width:1px;height:16px;background:var(--line)}
.hero-title{left:139px;top:198px;font-family:"Raleway",sans-serif;font-weight:500;font-size:41px;color:#333;letter-spacing:.3px}
.hero-sub{left:141px;top:248px;font-family:"Raleway",sans-serif;font-size:19.5px;color:#333}
.hero-sub b{font-weight:700}
.cta{left:140px;top:298px;width:150px;height:25px;background:var(--blue);border-bottom:2px solid var(--blue-dark);border-radius:3px;color:var(--white);font-family:"Raleway",sans-serif;font-weight:700;font-size:12.5px;display:flex;align-items:center;justify-content:center;gap:6px}
.slide-arrow{top:271px;width:29px;height:28px;background:var(--white);border:1px solid #ccc;display:flex;align-items:center;justify-content:center}

/* feature cards */
.card{top:483px;width:191px;height:191px;background:var(--white);border:1px solid #ddd;box-shadow:0 1px 2px rgba(0,0,0,.05);text-align:center}
.card h3{margin-top:17px;font-family:"Raleway",sans-serif;font-weight:500;font-size:16px;color:#333}
.card svg{display:block;margin:14px auto 0}
.card p{margin-top:14px;font-size:9.5px;line-height:12px;color:#444;padding:0 24px}
.learn{display:inline-block;margin-top:8px;width:65px;height:17px;line-height:15px;background:var(--blue);border-bottom:2px solid var(--blue-dark);border-radius:2px;color:var(--white);font-size:8.5px;font-weight:600}

/* solutions band */
.solutions{left:0;top:718px;width:1074px;height:299px;background:var(--gray-band)}
.notch{left:528px;top:718px}
.section-title{left:139px;top:737px;font-family:"Raleway",sans-serif;font-weight:500;font-size:20px;color:#222}
.kicker{font-size:8px;color:var(--blue);letter-spacing:.3px;text-transform:uppercase}
.solution{top:799px;width:200px;text-align:center}
.solution .photo{width:136px;height:136px;border-radius:50%;border:4px solid var(--white);margin:0 auto;box-shadow:0 1px 3px rgba(0,0,0,.15)}
.solution h4{margin-top:8px;font-family:"Raleway",sans-serif;font-weight:500;font-size:13px;color:#222}
.solution .kicker{margin-top:3px}

/* footer */
.footer{left:0;top:1017px;width:1074px;height:183px;background:var(--footer)}
.footer-brand{left:148px;top:1050px;display:flex;align-items:center;gap:6px;font-family:"Raleway",sans-serif;font-weight:700;font-size:24px;color:var(--white)}
.footer-brand .brand-dot{background:var(--white)}
.footer .social,.f-social{border-color:#777;background:#eee;width:23px;height:23px}
.copyright{left:150px;top:1150px;font-size:8px;color:#eee}
.footer-links{top:1051px;list-style:none;font-size:9.5px;line-height:13px;color:#eee}
.footer-divider{left:616px;top:1045px;width:1px;height:118px;background:#555}
.newsletter-title{left:690px;top:1044px;font-family:"Raleway",sans-serif;font-size:20px;color:var(--white)}
.field{left:690px;width:252px;height:25px;background:var(--white);font-size:9.5px;color:#444;padding:7px 15px}
.confirm{left:690px;top:1147px;font-size:10px;color:#999;display:flex;align-items:center;gap:6px}
.checkbox{width:9px;height:9px;background:#eee;border:1px solid #999;display:flex;align-items:center;justify-content:center}
.submit{left:858px;top:1145px;width:84px;height:21px;background:var(--blue);border-radius:2px;color:var(--white);font-size:11px;display:flex;align-items:center;justify-content:center}
</style>
</head>
<body>

<header class="abs topbar"></header>
<div class="abs brand"><span>LumaPort</span><span class="brand-dot"></span></div>
<div class="abs audience-tab tab-business">I'm a Business</div>
<div class="abs audience-tab tab-developer">I'm a Developer</div>
<div class="abs account-links">Login<span>|</span>Register<span>|</span>Contact Us</div>
<div class="abs social" style="left:820px;top:10px"></div>
<div class="abs social" style="left:860px;top:10px"></div>
<div class="abs social" style="left:899px;top:10px"></div>
<div class="abs social" style="left:937px;top:10px"></div>

<section class="abs hero" role="img" aria-label="Photo of a smiling businesswoman in glasses and a light blazer in a bright office"></section>

<nav class="abs main-nav">
  <a style="left:58px">Home</a><span class="nav-sep" style="left:97px"></span>
  <a style="left:142px">Solutions</a><span class="nav-sep" style="left:190px"></span>
  <a style="left:241px">Developers</a><span class="nav-sep" style="left:294px"></span>
  <a style="left:338px">Partners</a><span class="nav-sep" style="left:385px"></span>
  <a style="left:430px">Company</a><span class="nav-sep" style="left:478px"></span>
  <a style="left:528px">Resources</a><span class="nav-sep" style="left:580px"></span>
  <a style="left:612px">Blog</a>
</nav>

<h1 class="abs hero-title">Fast, Secure, Worldwide</h1>
<p class="abs hero-sub">LumaPort is your solution <b>to all payment needs</b></p>
<div class="abs cta">
  <svg width="12" height="12" viewBox="0 0 12 12"><path d="M2 10l1-3 5-5 2 2-5 5z" fill="#fff"/></svg>
  Sign Up Today!
</div>
<div class="abs slide-arrow" style="left:46px"><svg width="8" height="12" viewBox="0 0 8 12"><path d="M6 1L1 6l5 5" fill="none" stroke="#333" stroke-width="1.5"/></svg></div>
<div class="abs slide-arrow" style="left:1009px"><svg width="8" height="12" viewBox="0 0 8 12"><path d="M2 1l5 5-5 5" fill="none" stroke="#333" stroke-width="1.5"/></svg></div>

<article class="abs card" style="left:141px">
  <h3>CONSEQUUNTUR</h3>
  <svg width="44" height="44" viewBox="0 0 44 44"><g fill="var(--red)"><circle cx="22" cy="22" r="14"/><g transform="translate(22 22)"><rect x="-4" y="-21" width="8" height="10"/><rect x="-4" y="-21" width="8" height="10" transform="rotate(45)"/><rect x="-4" y="-21" width="8" height="10" transform="rotate(90)"/><rect x="-4" y="-21" width="8" height="10" transform="rotate(135)"/><rect x="-4" y="-21" width="8" height="10" transform="rotate(180)"/><rect x="-4" y="-21" width="8" height="10" transform="rotate(225)"/><rect x="-4" y="-21" width="8" height="10" transform="rotate(270)"/><rect x="-4" y="-21" width="8" height="10" transform="rotate(315)"/></g></g><circle cx="22" cy="22" r="7" fill="#fff"/><circle cx="22" cy="22" r="3.5" fill="var(--red)"/></svg>
  <p>Lorem ipsum dolor sit amet, con-sectetur adipiscing elit.</p>
  <span class="learn">Learn More</span>
</article>
<article class="abs card" style="left:350px">
  <h3>TEMPORIBUS</h3>
  <svg width="48" height="44" viewBox="0 0 48 44"><rect x="6" y="4" width="36" height="28" rx="2" fill="var(--red)"/><rect x="10" y="8" width="28" height="20" fill="#fff"/><path d="M16 18l5 5 10-10" fill="none" stroke="var(--red)" stroke-width="3.5"/><path d="M1 34h46v3a3 3 0 0 1-3 3H4a3 3 0 0 1-3-3z" fill="var(--red)"/></svg>
  <p>Lorem ipsum dolor sit amet, con-sectetur adipiscing elit.</p>
  <span class="learn">Learn More</span>
</article>
<article class="abs card" style="left:560px">
  <h3>OFFICIA DESERUNT</h3>
  <svg width="44" height="44" viewBox="0 0 44 44" fill="var(--red)"><circle cx="12" cy="9" r="5"/><circle cx="32" cy="9" r="5"/><rect x="5" y="15" width="14" height="16" rx="3"/><rect x="25" y="15" width="14" height="16" rx="3"/><circle cx="22" cy="13" r="6" stroke="#fff" stroke-width="1.5"/><rect x="14" y="20" width="16" height="22" rx="3" stroke="#fff" stroke-width="1.5"/></svg>
  <p>Lorem ipsum dolor sit amet, con-sectetur adipiscing elit.</p>
  <span class="learn">Learn More</span>
</article>
<article class="abs card" style="left:768px">
  <h3>LOREM IPSUM</h3>
  <svg width="46" height="44" viewBox="0 0 46 44"><rect x="8" y="8" width="34" height="20" rx="2" fill="var(--red)" transform="rotate(-12 25 18)"/><rect x="4" y="16" width="36" height="20" rx="2" fill="var(--red)" stroke="#fff" stroke-width="1.5"/><rect x="8" y="19" width="28" height="14" fill="none" stroke="#fff" stroke-width="1"/><circle cx="22" cy="26" r="5" fill="#fff"/><text x="22" y="29" font-size="8" font-weight="700" text-anchor="middle" fill="var(--red)" font-family="Arial,sans-serif">$</text></svg>
  <p>Lorem ipsum dolor sit amet, con-sectetur adipiscing elit.</p>
  <span class="learn">Learn More</span>
</article>

<section class="abs solutions"></section>
<svg class="abs notch" width="42" height="25" viewBox="0 0 42 25"><path d="M0 0h42L21 25z" fill="#fff"/></svg>
<h2 class="abs section-title">Proposed Solutions</h2>
<div class="abs kicker" style="left:140px;top:764px">Lorem ipsum dolor amet</div>

<div class="abs solution" style="left:198px">
  <div class="photo" role="img" aria-label="Portrait photo of a smiling businesswoman" style="background:radial-gradient(circle at 50% 45%,#d9b9a3,#8a7468 60%,#f1ede8)"></div>
  <h4>Deserunt mollitia animi</h4><div class="kicker">Lorem ipsum dolor amet</div>
</div>
<div class="abs solution" style="left:443px">
  <div class="photo" role="img" aria-label="Photo of a woman holding a payment card at a desk" style="background:radial-gradient(circle at 50% 40%,#e2c9aa,#b8a898 60%,#e6e2dc)"></div>
  <h4>Deserunt mollitia animi</h4><div class="kicker">Lorem ipsum dolor amet</div>
</div>
<div class="abs solution" style="left:686px">
  <div class="photo" role="img" aria-label="Photo of a hand with a blue card over a keyboard" style="background:linear-gradient(160deg,#3a98cf 0%,#7fb8d8 35%,#e6e6e6 60%,#c9c9c9 100%)"></div>
  <h4>Deserunt mollitia animi</h4><div class="kicker">Lorem ipsum dolor amet</div>
</div>

<footer class="abs footer"></footer>
<div class="abs footer-brand"><span>LumaPort</span><span class="brand-dot"></span></div>
<div class="abs social f-social" style="left:148px;top:1109px"></div>
<div class="abs social f-social" style="left:188px;top:1109px"></div>
<div class="abs social f-social" style="left:227px;top:1109px"></div>
<div class="abs social f-social" style="left:265px;top:1109px"></div>
<div class="abs copyright">© Copyright 2014. All Rights Reserved.</div>
<ul class="abs footer-links" style="left:361px">
  <li>Home</li><li>ePayment</li><li>eWallet</li><li>Online Merchant</li><li>Online Sells</li><li>Purchase Online</li><li>Bank Transfer</li><li>Wire Transfer</li>
</ul>
<ul class="abs footer-links" style="left:485px">
  <li>Privacy Policy</li><li>Terms of Use</li><li>Site Map</li><li>Contact Us</li><li>Every Solution</li><li>Become a Member</li><li>Register</li><li>Login</li>
</ul>
<div class="abs footer-divider"></div>
<h3 class="abs newsletter-title">Join Newsletter</h3>
<div class="abs field" style="top:1078px">Name</div>
<div class="abs field" style="top:1111px">Email</div>
<div class="abs confirm"><span class="checkbox"><svg width="7" height="7" viewBox="0 0 7 7"><path d="M1 3.5l1.8 1.8L6 1.5" fill="none" stroke="#1d86d6" stroke-width="1.4"/></svg></span>Confirm subscription</div>
<div class="abs submit">SUBMIT</div>

</body>
</html>
```